Web Design Project for DJ

We need a web design for a DJ. Our client is a freelance DJ who already has a regular gig at a major night club but is looking to expand his exposure. He is located in a major metropolitan area and is looking for further gigs. He is hoping to generate further business via the website, including bookings via the site.

For reference his pagelinker page is here https://www.pagelinker.example/pages/DJ-Vorn/730162948415207

Following face to face discussions with the client today we have made a few small alterations to the brief.  We are hoping to have some images uploaded shortly.

Target Market(s)

Event planners, night club owners, radio stations, younger age groups (16-35)

Industry/Entity Type

Business

Requirements
Must have
• Name is DJVorn, this should obviously feature prominently. His current business card is attached as an example.

Links to Pagelinker and Tunedrift

Cool, modern look, slightly edgy.

Site will be built in Joomla, so a front page and secondary page template is required.
Nice to have
• Blog style layout to front page featuring recent and upcoming gigs.

Secondary pages may include a more expansive blog, a list of upcoming gigs, and a booking form.

Darker colour palettes preferred and use of same/similar fonts to those on the business card are an obvious plus

```html
<!DOCTYPE html>
<html lang="en">
<head>
<meta charset="utf-8">
<title>DJVorn</title>
<link href="https://fonts.googleapis.com/css2?family=Exo+2:wght@400;500;600&display=swap" rel="stylesheet">
<style>
:root{
  --bg:#181818;
  --bg-glow:#353535;
  --panel:#101010;
  --panel-border:#333;
  --text:#e6e6e6;
  --muted:#9a9a9a;
  --accent:#5aa8ff;
  --accent-bright:#7fbfff;
  --rule:#1e7fd8;
  --row-line:#262626;
}
*{margin:0;padding:0;box-sizing:border-box}
html,body{width:880px;height:1200px;overflow:hidden}
body{
  position:relative;
  background:radial-gradient(ellipse 420px 160px at 330px 40px,var(--bg-glow),transparent 80%),var(--bg);
  font-family:"Exo 2",sans-serif;color:var(--text);
}
.logo{position:absolute;left:62px;top:34px;font-size:56px;font-weight:500;color:var(--accent-bright);letter-spacing:1px;line-height:1}
.nav{position:absolute;top:58px;right:64px;display:flex;gap:28px;font-size:13.5px;letter-spacing:.5px}
.nav a{color:var(--text);text-decoration:none}
.nav a.book{color:var(--accent);font-weight:600}
.hero{position:absolute;left:64px;top:120px;width:752px;height:278px}
.hero-photo{position:absolute;inset:0;background:radial-gradient(ellipse at 50% 40%,#3d6bff,#1435a8 45%,#0a1640 90%)}
.hero svg{position:absolute;inset:0}
.section-title{position:absolute;font-size:14px;font-weight:600;letter-spacing:1px;display:flex;align-items:center;gap:9px}
.section-title::before{content:"";border-left:6px solid var(--text);border-top:4px solid transparent;border-bottom:4px solid transparent}
.news-title{left:64px;top:448px}
.news-rule{position:absolute;left:64px;top:475px;width:432px;height:1px;background:var(--rule)}
.headline{position:absolute;left:65px;font-size:19px;font-weight:400;letter-spacing:.4px}
.date{position:absolute;left:64px;font-size:17px;color:var(--accent);line-height:23px}
.body{position:absolute;left:112px;width:376px;font-size:10.6px;line-height:16.8px;color:var(--muted)}
.news-photo{position:absolute;left:111px;top:697px;width:306px;height:161px;border:1px solid #2a4aa8;background:radial-gradient(ellipse at 50% 30%,#4a7fd0,#2a2f6a 55%,#1a0f1e)}
.gigs{position:absolute;left:576px;top:438px;width:240px;height:412px;background:var(--panel);border:1px solid var(--panel-border)}
.gigs .section-title{left:15px;top:11px}
.gigs-rule{position:absolute;left:0;top:37px;width:100%;height:1px;background:var(--panel-border)}
.gigs table{position:absolute;left:16px;top:62px;width:168px;border-collapse:collapse;font-size:9.5px}
.gigs th{text-align:left;color:var(--accent);font-weight:500;height:16px;padding-left:7px}
.gigs td{height:32px;padding-left:7px;border-top:1px solid var(--row-line)}
.gigs tr:nth-child(2) td{border-top:none}
.gigs th:first-child,.gigs td:first-child{width:72px}
.footer-rule{position:absolute;left:128px;top:1155px;width:624px;height:1px;background:var(--rule)}
.copyright{position:absolute;top:1168px;width:100%;text-align:center;font-size:11px;color:var(--muted)}
</style>
</head>
<body>
<div class="logo">DJVORN</div>
<nav class="nav"><a href="#">GIGS.</a><a href="#">PHOTOS.</a><a href="#">CONTACT.</a><a href="#" class="book">BOOK NOW.</a></nav>

<div class="hero">
  <div class="hero-photo" role="img" aria-label="Concert stage with blue lights above a large crowd"></div>
  <svg width="752" height="278" viewBox="0 0 752 278">
    <polygon points="0,0 124,0 0,124" fill="#202020"/>
    <polygon points="752,150 752,278 630,278" fill="#202020"/>
    <polyline points="24,58 24,24 60,24" fill="none" stroke="#9a9a9a" stroke-width="2"/>
    <polyline points="692,254 728,254 728,220" fill="none" stroke="#5aa8ff" stroke-width="2"/>
    <rect x="0.5" y="0.5" width="751" height="277" fill="none" stroke="#1a2f66"/>
  </svg>
</div>

<div class="section-title news-title">LATEST NEWS</div>
<div class="news-rule"></div>

<h2 class="headline" style="top:498px">News Headline nr. One</h2>
<div class="date" style="top:534px">23/<br>06</div>
<p class="body" style="top:534px">Lorem ipsum dolor sit amet, consectetur adipiscing elit. Dolere malum est: in crucem qui agitur, beatus esse non potest. Nosti, credo, illud: Nemo pius est, qui pietatem; Itaque his sapiens semper vacabit. Duo Reges: constructio interrete. Non est ista, inquam...</p>

<h2 class="headline" style="top:658px">News Headline nr. Two</h2>
<div class="date" style="top:694px">22/<br>05</div>
<div class="news-photo" role="img" aria-label="Crowded club in front of a lit stage"></div>
<p class="body" style="top:870px">Lorem ipsum dolor sit amet, consectetur adipiscing elit. Dolere malum est: in crucem qui agitur, beatus esse non potest. Nosti, credo, illud: Nemo pius est, qui pietatem; Itaque his sapiens semper vacabit. Duo Reges: constructio interrete. Non est ista, inquam...</p>

<h2 class="headline" style="top:986px">News Headline nr. Three</h2>
<div class="date" style="top:1022px">21/<br>04</div>
<p class="body" style="top:1022px">Lorem ipsum dolor sit amet, consectetur adipiscing elit. Dolere malum est: in crucem qui agitur, beatus esse non potest. Nosti, credo, illud: Nemo pius est, qui pietatem; Itaque his sapiens semper vacabit. Duo Reges: constructio interrete. Non est ista, inquam...</p>

<aside class="gigs">
  <div class="section-title">UPCOMING GIGS</div>
  <div class="gigs-rule"></div>
  <table>
    <tr><th>Date</th><th>Venue</th></tr>
    <tr><td>01 Jan</td><td>Venue name nr.1</td></tr>
    <tr><td>02 Feb</td><td>Venue name nr.2</td></tr>
    <tr><td>03 Mar</td><td>Venue name nr.3</td></tr>
    <tr><td>04 Apr</td><td>Venue name nr.4</td></tr>
    <tr><td>05 May</td><td>Venue name nr.5</td></tr>
    <tr><td>06 Jun</td><td>Venue name nr.6</td></tr>
    <tr><td>07 Jul</td><td>Venue name nr.7</td></tr>
    <tr><td>08 Aug</td><td>Venue name nr.8</td></tr>
    <tr><td>09 Sep</td><td>Venue name nr.9</td></tr>
    <tr><td>10 Oct</td><td>Venue name nr.10</td></tr>
  </table>
</aside>

<div class="footer-rule"></div>
<p class="copyright">© Copyright DJVorn 2013. All rights reserved.</p>
</body>
</html>
```